Website Layout for PanFolio

PanFolio is a company that will be dedicated (for now) to publishing recipes with the nutrition facts. Run by a nutritionist. In the future there may be a mobile app.

We need layout for 3 of the pages of the website. NO PROGRAMMING, only layout and graphic design. Not very complicated.

--Please view the details in the attached document--
We want a layout design for the pages: P.01, P.02 and P.03

Logo is also attached. Please don't hesitate if you want to modify the logo to fit your idea. The design should be clean, visually attractive and refreshing to look at. It should be sleek and a feel of technology, yet also natural and culinary.

Some examples to get ideas:

http://www.marlowhearthtales.com/
http://www.tavelbrunefare.org/site/
http://thecobaltladle.com/products/dice-deck
Updates

Project Deadline Extended
Reason: I extend the deadline for this week to allow you space for work on the observations made to your design and to provide the P.02 and P.03 designs. We greatly appreciate your hard work and are thrilled with your ideas.

Target Market(s)

Young people that live alone or want to optimize their cooking.
Young, modern housewives with a smartphone.

Industry/Entity Type

Nutrition

Requirements
Must have
• --Please view the details in the attached document--
NO PROGRAMMING. Only layout and graphic design.

```html
<!DOCTYPE html>
<html lang="en">
<head>
<meta charset="utf-8">
<title>PanFolio</title>
<link href="https://fonts.googleapis.com/css2?family=Open+Sans:ital,wght@0,400;0,600;0,700;1,400&family=Amatic+SC:wght@700&display=swap" rel="stylesheet">
<style>
  :root{
    --white:#ffffff;
    --ink:#3a3a3a;
    --muted:#7a7a7a;
    --line:#d4d4d4;
    --accent:#e8532b;
    --green:#9bc53d;
    --green-dot:#8cc63f;
    --gold:#f2b01e;
    --shade:rgba(28,24,20,0.86);
    --card-text:#f1ece6;
  }
  *{box-sizing:border-box;margin:0;padding:0}
  html,body{width:914px;height:1200px;overflow:hidden;background:var(--white);font-family:"Open Sans",Arial,sans-serif}
  .page{position:relative;width:914px;height:1200px}

  .hero{position:absolute;left:0;top:0;width:914px;height:376px;
    background:radial-gradient(ellipse 260px 190px at 470px 190px,#d9cbb4 0%,#b69a74 45%,rgba(0,0,0,0) 75%),
    radial-gradient(ellipse 90px 80px at 700px 140px,#a5272b 0%,rgba(0,0,0,0) 100%),
    linear-gradient(180deg,#3b2e22 0%,#6d5c4d 45%,#8b7d70 100%)}
  .hero-shade{position:absolute;inset:0;background:rgba(0,0,0,0.18)}
  .topbar{position:absolute;top:8px;left:636px;display:flex;gap:4px;align-items:center}
  .menu-btn{width:21px;height:19px;background:#5a5a5a;display:flex;align-items:center;justify-content:center}
  .btn{height:19px;width:53px;font-size:10px;font-weight:600;display:flex;align-items:center;justify-content:center}
  .btn-login{background:var(--white);color:#666}
  .btn-join{background:var(--accent);color:var(--white)}
  .brand{position:absolute;top:150px;left:0;width:914px;display:flex;justify-content:center;align-items:center;gap:10px}
  .brand-mark{width:30px;height:30px;background:var(--green)}
  .brand-name{font-size:32px;font-weight:600;color:var(--white)}
  .tagline{position:absolute;top:209px;left:0;width:914px;text-align:center;color:var(--white);font-size:12.5px}
  .dots{position:absolute;top:357px;left:748px;display:flex;gap:3px}
  .dots span{width:6px;height:6px;border-radius:50%;background:rgba(255,255,255,0.45)}
  .dots span.on{background:var(--green-dot)}

  .search{position:absolute;left:634px;top:409px;width:137px;height:20px;border:1px solid var(--line);
    font-size:9.5px;font-weight:600;color:var(--muted);padding:0 8px;display:flex;align-items:center;justify-content:space-between}

  .card{position:absolute;width:152px;overflow:hidden;border-radius:2px}
  .photo{position:absolute;inset:0}
  .caption{position:absolute;left:0;right:0;bottom:0;background:var(--shade);padding:8px 14px 0 16px;color:var(--card-text)}
  .caption h3{font-family:"Amatic SC","Arial Narrow",sans-serif;font-size:21px;line-height:22px;font-weight:700;letter-spacing:0.5px}
  .caption p{font-size:8px;line-height:9.5px;margin-top:2px}
  .caption .facts{font-size:6px;font-style:italic;margin-top:10px}
  .card.active .caption h3,.card.active .caption .facts{color:var(--gold)}
  .bites{position:absolute;top:6px;left:8px;display:flex;height:22px;border:1px solid #ccc;background:var(--white)}
  .bites .label{width:54px;font-size:9px;font-weight:600;color:#444;display:flex;align-items:center;justify-content:center;border-right:1px solid #ccc}
  .bites .like{width:20px;display:flex;align-items:center;justify-content:center}

  .footer{position:absolute;left:0;top:1012px;width:914px;height:188px;background:var(--green);color:var(--white);text-align:center}
  .social{position:absolute;top:55px;left:412px;display:flex;gap:4px}
  .social span{width:27px;height:27px;border-radius:50%;background:var(--white)}
  .rule{position:absolute;top:88px;width:914px;font-size:7px}
  .links{position:absolute;top:104px;width:914px;font-size:8.5px;display:flex;justify-content:center;gap:10px}
  .copy{position:absolute;top:126px;width:914px;font-size:9.5px}
</style>
</head>
<body>
<div class="page">
  <header class="hero">
    <div class="hero-shade" role="img" aria-label="Photo of an oat pancake with banana slices and strawberries on a plate"></div>
    <nav class="topbar">
      <div class="menu-btn"><svg width="11" height="9" viewBox="0 0 11 9"><rect y="0" width="11" height="1.6" fill="#fff"/><rect y="3.7" width="11" height="1.6" fill="#fff"/><rect y="7.4" width="11" height="1.6" fill="#fff"/></svg></div>
      <div class="btn btn-login">Login</div>
      <div class="btn btn-join">Join Us</div>
    </nav>
    <div class="brand"><span class="brand-mark"></span><span class="brand-name">PanFolio</span></div>
    <p class="tagline">Lorem ipsum dolor sit amet, consectetur adipisicing elit</p>
    <div class="dots"><span class="on"></span><span></span><span></span></div>
  </header>

  <div class="search"><span>Search</span>
    <svg width="9" height="9" viewBox="0 0 10 10"><circle cx="4" cy="4" r="3" fill="none" stroke="#888" stroke-width="1.5"/><line x1="6.2" y1="6.2" x2="9.2" y2="9.2" stroke="#888" stroke-width="1.6"/></svg>
  </div>

  <article class="card active" style="left:143px;top:458px;height:233px">
    <div class="photo" role="img" aria-label="Glass bowl of sliced bananas and oats" style="background:linear-gradient(170deg,#e9d7c7,#c98d52 55%,#6b4a33)"></div>
    <div class="bites"><span class="label">Bites It</span><span class="like"><svg width="12" height="12" viewBox="0 0 12 12"><path d="M1 5h2v6H1zM4 5l2.5-4c1 0 1.3.7 1.1 1.7L7.2 4.5H10.5c.7 0 1.1.6.9 1.2l-1.2 4.5c-.2.5-.6.8-1.1.8H4z" fill="none" stroke="#555" stroke-width="0.9"/></svg></span></div>
    <div class="caption" style="height:77px"><h3>Breakfast</h3><p>Lorem ipsum dolor sit amet consectetur</p><div class="facts">Calories 1XX0 &nbsp;-&nbsp; Fat Time 1XX</div></div>
  </article>
  <article class="card" style="left:143px;top:698px;height:239px">
    <div class="photo" role="img" aria-label="Burger with bacon and lettuce" style="background:linear-gradient(180deg,#5f8f3a,#8a4a2a 60%,#3a2418)"></div>
    <div class="caption" style="height:78px"><h3>Full Meals</h3><p>Lorem ipsum dolor sit amet consectetur</p><div class="facts">Calories 1XX0 &nbsp;-&nbsp; Fat Time 1XX</div></div>
  </article>

  <article class="card" style="left:302px;top:458px;height:284px">
    <div class="photo" role="img" aria-label="Spinach and feta mini muffins on a white plate" style="background:linear-gradient(160deg,#6a5030,#c2a874 45%,#e6e0d4 70%,#8c7a5a)"></div>
    <div class="caption" style="height:77px"><h3>Pastry</h3><p>Lorem ipsum dolor sit amet consectetur</p><div class="facts">Calories 1XX0 &nbsp;-&nbsp; Fat Time 1XX</div></div>
  </article>
  <article class="card" style="left:302px;top:749px;height:181px">
    <div class="photo" role="img" aria-label="Nut-coated cheese balls with olives" style="background:linear-gradient(170deg,#c9c2b6,#d9b984 50%,#6c6a58)"></div>
    <div class="caption" style="height:77px"><h3>Category Name</h3><p>Lorem ipsum dolor sit amet consectetur</p><div class="facts">Calories 1XX0 &nbsp;-&nbsp; Fat Time 1XX</div></div>
  </article>

  <article class="card" style="left:461px;top:458px;height:245px">
    <div class="photo" role="img" aria-label="Seeded crispbread squares" style="background:linear-gradient(160deg,#5a4a3c,#8e7b68 50%,#3e3128)"></div>
    <div class="caption" style="height:77px"><h3>Soups</h3><p>Lorem ipsum dolor sit amet consectetur</p><div class="facts">Calories 1XX0 &nbsp;-&nbsp; Fat Time 1XX</div></div>
  </article>
  <article class="card" style="left:461px;top:710px;height:244px">
    <div class="photo" role="img" aria-label="Puff pastries with berry jam" style="background:linear-gradient(170deg,#f1d58e,#e3a75a 45%,#a8283a 70%,#d8c3a0)"></div>
    <div class="caption" style="height:77px"><h3>Category Name</h3><p>Lorem ipsum dolor sit amet consectetur</p><div class="facts">Calories 1XX0 &nbsp;-&nbsp; Fat Time 1XX</div></div>
  </article>

  <article class="card" style="left:620px;top:458px;height:182px">
    <div class="photo" role="img" aria-label="Sandwich with avocado and lentils on a blue plate" style="background:linear-gradient(170deg,#7a5a3a,#5f9ab0 45%,#8a4a22)"></div>
    <div class="caption" style="height:77px"><h3>Snacks</h3><p>Lorem ipsum dolor sit amet consectetur</p><div class="facts">Calories 1XX0 &nbsp;-&nbsp; Fat Time 1XX</div></div>
  </article>
  <article class="card" style="left:620px;top:646px;height:216px">
    <div class="photo" role="img" aria-label="Mini pizza bites with basil and tomato sauce" style="background:linear-gradient(170deg,#5c6e78,#e4c47c 45%,#c99a5a 75%,#4a4038)"></div>
    <div class="caption" style="height:77px"><h3>Category Name</h3><p>Lorem ipsum dolor sit amet consectetur</p><div class="facts">Calories 1XX0 &nbsp;-&nbsp; Fat Time 1XX</div></div>
  </article>

  <footer class="footer">
    <div class="social"><span></span><span></span><span></span></div>
    <div class="rule">-----</div>
    <nav class="links"><span>Home</span><span>About Us</span><span>Contact Us</span><span>Terms</span></nav>
    <p class="copy">© Copyright 2014</p>
  </footer>
</div>
</body>
</html>
```